Banner poster with different motifs

I'm looking for 5 banners and posters in A1 format in the same design, or the similarity must be recognizable...
Kept quite simple with different titles.

1 ballet
2 Contemporary Dance
3 high heels
4 Salsa & Bachata & Zouk
5 Hip Hop

Modern bright colors
it is for the entrance so that the students see here is a dance school

The text may also be included in the image
The photos are for guidance only; some are our own, some are purchased. However, we are permitted to use them, including our logo, of course.

```html
<!DOCTYPE html>
<html lang="de">
<head>
<meta charset="utf-8">
<title>Hip Hop – Movimento Dance Center</title>
<link rel="stylesheet" href="https://fonts.googleapis.com/css2?family=Poppins:wght@300;400;600;700&display=swap">
<style>
  :root {
    --page: #ffffff;
    --magenta: #83114f;
    --navy: #222c4a;
    --ink: #222222;
    --haze-light: #fbfbfc;
    --haze-mid: #dcdcdf;
    --floor: #9a9a9e;
  }
  html, body {
    margin: 0;
    width: 1200px;
    height: 1037px;
    overflow: hidden;
    background: var(--page);
    font-family: "Poppins", sans-serif;
  }
  .poster {
    position: absolute;
    left: 73px;
    top: 163px;
    width: 1055px;
    height: 746px;
    overflow: hidden;
    background:
      radial-gradient(ellipse 55% 45% at 58% 18%, var(--haze-light) 0%, rgba(255,255,255,0) 70%),
      linear-gradient(180deg, #e4e4e7 0%, #f2f2f4 40%, #e6e6e9 72%, var(--floor) 82%, #c9c9cc 100%);
  }
  .dancer-photo {
    position: absolute;
    left: 11px;
    top: 89px;
    width: 591px;
    height: 570px;
    border-radius: 40% 30% 35% 45%;
    background: radial-gradient(ellipse at 55% 40%, rgba(150,120,110,0.55) 0%, rgba(150,140,145,0.35) 45%, rgba(220,220,224,0) 75%);
  }
  .headline {
    position: absolute;
    left: 0;
    top: 0;
    width: 1055px;
    height: 746px;
  }
  .headline text { font-family: "Poppins", sans-serif; font-weight: 700; }
  .word-hip { fill: var(--magenta); }
  .word-hop { fill: var(--navy); }
  .brand {
    position: absolute;
    left: 86px;
    top: 435px;
    width: 236px;
    text-align: center;
    color: var(--ink);
  }
  .brand-mark {
    display: block;
    width: 86px;
    height: 86px;
    margin: 0 auto 14px;
    border: 1.5px solid var(--ink);
    border-radius: 50%;
    box-sizing: border-box;
  }
  .brand-name {
    margin: 0;
    font-weight: 300;
    font-size: 35px;
    line-height: 1;
    letter-spacing: 1px;
  }
  .brand-tagline {
    margin: 6px 0 0;
    font-weight: 400;
    font-size: 10.5px;
    letter-spacing: 3.2px;
    white-space: nowrap;
  }
  .website {
    position: absolute;
    left: 506px;
    top: 660px;
    margin: 0;
    font-size: 33px;
    line-height: 1;
    letter-spacing: 3px;
    color: var(--ink);
    white-space: nowrap;
  }
  .website strong { color: var(--magenta); font-weight: 700; }
</style>
</head>
<body>
  <main class="poster">
    <div class="dancer-photo" role="img" aria-label="Photo of a hip hop dancer in a crop top and grey sweatpants, leaning far back with long hair flying, on a bright studio floor with light rays"></div>

    <svg class="headline" viewBox="0 0 1055 746" aria-label="Hip Hop">
      <text class="word-hip" x="503" y="0" font-size="272" textLength="471" lengthAdjust="spacingAndGlyphs" transform="translate(0,335) scale(1,1.5)">HIP</text>
      <text class="word-hop" x="503" y="0" font-size="211" textLength="471" lengthAdjust="spacingAndGlyphs" transform="translate(0,609) scale(1,1.72)">HOP</text>
    </svg>

    <div class="brand">
      <span class="brand-mark" aria-hidden="true"></span>
      <p class="brand-name">MOVIMENTO</p>
      <p class="brand-tagline">DANCE CENTER FRANKFURT</p>
    </div>

    <p class="website">www.<strong>movimento-tanz</strong>.de</p>
  </main>
</body>
</html>
```